Martial Arts Website

Redevelopment of existing martial arts website.

The academy teaches traditional shaolin martial arts, including Shaolin Kung Fu, Wu Shu, Tai Chi, Qigong and Wing Chun and the site needs to reflect the traditional roots (eg, no tacky boxing imagery)

Existing website is www.copperheron.com.au to get a feel for the desired color scheme (black, green and red). The exact colors can be tweaked though. Please only reuse the logo and font (Karate) - there isnt anything else from the current design that needs to remain.

The current website includes links to a ClipTube channel that includes demonstrations of the training conducted to better guide the design.

The new website site map will be:
1. Home
2. Programs - summary page describing each form of training
a. Tiny Otters
b. Kids Kung Fu
c. Youth Kung Fu
d. Adults Kung Fu
e. Wing Chun
f. Tai Chi & Qigong
g. Weaponry Classes
h. 72 Arts of Shaolin Conditioning Program
i. Acrobatics and Wu Shu
j. Fitness Boxing
3. Timetable
4. Coaches - summary page describing all coaches
a. Sifu (Master)
b. Sihing Lou
c. Sihing Kim
d. Sihing Felix
X. ... up to 10 or so coaches
5. Member Zone
6. Contact Us
Updates

Logo now attached to brief - sorry I only have it in PDF

Just to clarify, I am only expecting a PSD design - no HTML required

Reason: Thanks for the designs, we love a lot of them just require a little extra time to tweak the designs and establish the potential. Thanks for your understanding and efforts.

Target Market(s)

Parents, teenagers, young adults, adults, elderly

Industry/Entity Type

Training

Requirements
Must have
• Chinese kung fu dragon imagery throughout the background
Links to Facenote and ClipTube channel
Promo/icon in the header "Try 2 free classes now"
Home page should include an embedded ClipTube video

```html
<!DOCTYPE html>
<html lang="en">
<head>
<meta charset="utf-8">
<title>Copper Heron Martial Arts Academy</title>
<link href="https://fonts.googleapis.com/css2?family=Arimo:wght@400;700&display=swap" rel="stylesheet">
<style>
:root{
  --ink:#1c1c1c;
  --nav:#262626;
  --hero:#3b3b3b;
  --green:#1fc45a;
  --logo-green:#27b04a;
  --red:#d10a0a;
  --red-dark:#9c0000;
  --white:#ffffff;
  --text:#222222;
  --muted:#bdbdbd;
  --footer:#050505;
  --bar:#1f1f1f;
}
*{box-sizing:border-box;margin:0;padding:0}
html,body{width:1010px;height:1200px;overflow:hidden;background:var(--ink);font-family:"Arimo",Arial,sans-serif}
.page{position:relative;width:1010px;height:1200px}
.abs{position:absolute}

/* header */
.header{left:0;top:0;width:1010px;height:85px;background:linear-gradient(#242424,#171717)}
.brand-mark{left:75px;top:4px;width:76px;height:76px;border-radius:50%;background:#0f2a16;border:3px solid var(--logo-green)}
.brand-name{left:162px;top:26px;font-size:21px;font-weight:700;color:var(--logo-green);letter-spacing:.5px}
.brand-tag{left:232px;top:55px;font-size:8.5px;color:#9a9a9a;letter-spacing:1.4px}
.social-top{left:882px;top:14px;display:flex;gap:6px}
.social-chip{width:22px;height:22px;border-radius:3px;font-size:7px;font-weight:700;color:#fff;display:flex;align-items:center;justify-content:center}
.chip-blue{background:#2f5fa8}
.chip-red{background:#c4161c;border:2px solid #eee}
.search{left:751px;top:52px;width:185px;height:23px;border-radius:12px;background:#2b2b2b;border:1px solid #444;color:#aaa;font-size:10px;padding:5px 11px}
.search svg{position:absolute;right:9px;top:5px}

/* nav */
.nav{left:0;top:85px;width:1010px;height:41px;background:linear-gradient(#2c2c2c,#1c1c1c);border-top:1px solid #333;display:flex;padding-left:74px}
.nav-item{height:41px;display:flex;align-items:center;gap:10px;padding:0 14px;color:#eee;font-size:12px;border-right:1px solid #121212;border-left:1px solid #383838}
.nav-item.active{background:#1a1a1a;box-shadow:inset 0 3px 0 var(--green)}
.caret{width:13px;height:13px;border-radius:50%;border:1px solid #777;background:#333;display:flex;align-items:center;justify-content:center}

/* hero */
.hero{left:0;top:126px;width:1010px;height:340px;background:radial-gradient(circle at 30% 40%,#4d4d4d,#333 70%)}
.bokeh{position:absolute;border-radius:50%;background:rgba(255,255,255,.06)}
.hero-title{left:132px;top:82px;width:300px;color:#fff;font-size:15.5px;line-height:20px}
.hero-copy{left:132px;top:145px;width:300px;color:#eee;font-size:11px;line-height:20px}
.cta{left:131px;top:210px;width:247px;height:41px;border-radius:9px;background:linear-gradient(#f2605a 0,#e21b1b 30%,#b70000);border:1px solid #ff6b6b;color:#fff;font-size:20px;display:flex;align-items:center;justify-content:center;box-shadow:0 2px 4px rgba(0,0,0,.5)}
.photo-frame{left:459px;top:17px;width:444px;height:294px;background:#fff;padding:6px}
.photo{width:100%;height:100%;background:linear-gradient(#5a6a55 0%,#8b8f7c 35%,#6f9a3a 60%,#7fb23a 100%)}
.arrow{top:147px;width:31px;height:38px;border-radius:4px;display:flex;align-items:center;justify-content:center}
.arrow-prev{left:64px;background:#111}
.arrow-next{left:917px;background:var(--green)}

.dots-band{left:0;top:466px;width:1010px;height:19px;background:#222;border-top:2px solid #666}
.dots-tab{left:456px;top:453px;width:100px;height:30px;border-radius:14px 14px 0 0;background:#222;border:2px solid #666;border-bottom:none;display:flex;justify-content:center;align-items:center;gap:5px}
.dot{width:12px;height:12px;border-radius:50%;border:2px solid #ddd;background:#222}
.dot.on{background:var(--green)}

/* content */
.content-bg{left:0;top:485px;width:1010px;height:447px;background:linear-gradient(90deg,#5a5a5a,#8e8e8e 30%,#9a9a9a 50%,#8e8e8e 70%,#5a5a5a)}
.panel{left:74px;top:506px;width:861px;height:399px;background:#fff;border-radius:5px}
.card{top:527px;width:248px;height:353px;border:1px solid #ccc;border-radius:12px;background:#fff}
.card-head{height:41px;border-radius:10px 10px 6px 6px;background:linear-gradient(#e35a55 0,#d41515 25%,#a70000);color:#fff;font-size:20px;padding:9px 24px;margin:-1px -1px 0}
.class-list{list-style:none;padding:20px 0 0 26px}
.class-list li{position:relative;padding-left:20px;margin-bottom:13px}
.class-list li svg{position:absolute;left:0;top:3px}
.class-name{font-size:15px;font-weight:700;color:var(--text)}
.class-age{font-size:12px;color:var(--text);margin-top:3px}
.more{position:absolute;right:24px;bottom:19px;width:58px;height:25px;border-radius:10px;background:linear-gradient(#ddd,#b0a9a9);border:1px solid #999;font-size:11px;color:#333;display:flex;align-items:center;justify-content:center}
.video{position:absolute;left:18px;top:56px;width:213px;height:203px;background:#000}
.video-copy{position:absolute;left:18px;top:270px;width:213px;font-size:11px;line-height:15px;color:var(--text);text-align:justify}
.about{padding:17px 14px 0 24px;font-size:9.8px;line-height:16.8px;color:#333;text-align:justify}
.about p{margin-bottom:9px}
.about b{font-size:15px;color:var(--red);font-weight:400}

/* footer */
.footer{left:0;top:932px;width:1010px;height:230px;background:var(--footer)}
.f-title{font-size:20px;color:#eee}
.badge{top:985px;height:52px}
.divider{top:950px;width:1px;height:196px;background:#444}
.news{left:327px;top:990px;width:290px;list-style:none}
.news li{position:relative;padding-left:22px;color:#eee;font-size:12px;line-height:17px;margin-bottom:17px;text-align:justify}
.news li svg{position:absolute;left:0;top:3px}
.follow{left:690px;top:987px;display:flex;gap:11px}
.newsletter{left:690px;top:1034px;width:248px;height:41px;border-radius:9px;background:linear-gradient(#f2605a 0,#e21b1b 30%,#b70000);border:1px solid #ff6b6b;color:#fff;font-size:20px;display:flex;align-items:center;justify-content:center}
.bottom{left:0;top:1162px;width:1010px;height:38px;background:var(--bar);color:#eee;font-size:10.5px;display:flex;justify-content:space-between;align-items:center;padding:0 45px 0 74px}
</style>
</head>
<body>
<div class="page">

<header class="abs header">
  <div class="abs brand-mark"></div>
  <div class="abs brand-name">Copper Heron Martial Arts Academy</div>
  <div class="abs brand-tag">TRADITIONAL KUNG FU &amp; TAI CHI TRAINING CENTRE</div>
  <div class="abs social-top">
    <div class="social-chip chip-blue">Fn</div>
    <div class="social-chip chip-red">Ct</div>
  </div>
  <div class="abs search">Search...
    <svg width="12" height="12" viewBox="0 0 12 12"><circle cx="5" cy="5" r="3.8" fill="none" stroke="#777" stroke-width="1.5"/><line x1="8" y1="8" x2="11" y2="11" stroke="#777" stroke-width="1.8"/></svg>
  </div>
</header>

<nav class="abs nav">
  <div class="nav-item active">Home <span class="caret"><svg width="7" height="5"><path d="M0.5 0.5 3.5 4 6.5 0.5" fill="none" stroke="#ddd" stroke-width="1.2"/></svg></span></div>
  <div class="nav-item">Programs <span class="caret"><svg width="7" height="5"><path d="M0.5 0.5 3.5 4 6.5 0.5" fill="none" stroke="#ddd" stroke-width="1.2"/></svg></span></div>
  <div class="nav-item">Timetable <span class="caret"><svg width="7" height="5"><path d="M0.5 0.5 3.5 4 6.5 0.5" fill="none" stroke="#ddd" stroke-width="1.2"/></svg></span></div>
  <div class="nav-item">Coaches &nbsp; <span class="caret"><svg width="7" height="5"><path d="M0.5 0.5 3.5 4 6.5 0.5" fill="none" stroke="#ddd" stroke-width="1.2"/></svg></span></div>
  <div class="nav-item" style="padding:0 20px 0 22px">Member Zone &nbsp; <span class="caret"><svg width="7" height="5"><path d="M0.5 0.5 3.5 4 6.5 0.5" fill="none" stroke="#ddd" stroke-width="1.2"/></svg></span></div>
  <div class="nav-item" style="border-right:none">Contact Us</div>
</nav>

<section class="abs hero">
  <span class="bokeh" style="left:10px;top:40px;width:80px;height:80px"></span>
  <span class="bokeh" style="left:100px;top:165px;width:28px;height:28px"></span>
  <span class="bokeh" style="left:322px;top:255px;width:34px;height:34px"></span>
  <span class="bokeh" style="left:395px;top:90px;width:26px;height:26px"></span>
  <span class="bokeh" style="left:905px;top:60px;width:60px;height:60px"></span>
  <span class="bokeh" style="left:915px;top:208px;width:30px;height:30px"></span>
  <span class="bokeh" style="left:975px;top:185px;width:30px;height:30px"></span>
  <div class="abs hero-title">Welcome to Copper Heron Martial Arts Academy - NSW Australia</div>
  <div class="abs hero-copy">Traditional Shaolin Kung Fu, Wing Chun Kung Fu, Tai Chi &amp; Qigong for all ages and physical capabilities.</div>
  <div class="abs cta">Try 2 free classes NOW</div>
  <div class="abs photo-frame"><div class="photo" role="img" aria-label="Photo of a kung fu student performing a low kick on grass at an outdoor festival"></div></div>
  <div class="abs arrow arrow-prev"><svg width="12" height="10"><path d="M11 5H2M5.5 1 1.5 5 5.5 9" fill="none" stroke="#fff" stroke-width="2"/></svg></div>
  <div class="abs arrow arrow-next"><svg width="12" height="10"><path d="M1 5h9M6.5 1 10.5 5 6.5 9" fill="none" stroke="#fff" stroke-width="2"/></svg></div>
</section>

<div class="abs dots-band"></div>
<div class="abs dots-tab"><span class="dot on"></span><span class="dot"></span><span class="dot"></span><span class="dot"></span></div>

<section class="abs content-bg" role="img" aria-label="Faint grey Chinese dragon artwork in the background"></section>
<div class="abs panel"></div>

<article class="abs card" style="left:94px">
  <h2 class="card-head" style="font-weight:400">Classes</h2>
  <ul class="class-list">
    <li><svg width="12" height="10"><path d="M0 0 12 5 0 10 3 5Z" fill="#d10a0a"/></svg><div class="class-name">Tiny Otters</div><div class="class-age">Ages 4 to 6</div></li>
    <li><svg width="12" height="10"><path d="M0 0 12 5 0 10 3 5Z" fill="#d10a0a"/></svg><div class="class-name">Kids Kung Fu</div><div class="class-age">Ages 6 to 11</div></li>
    <li><svg width="12" height="10"><path d="M0 0 12 5 0 10 3 5Z" fill="#d10a0a"/></svg><div class="class-name">Youth Kung Fu</div><div class="class-age">Ages 11 to 15</div></li>
    <li><svg width="12" height="10"><path d="M0 0 12 5 0 10 3 5Z" fill="#d10a0a"/></svg><div class="class-name">Adults Kung Fu</div><div class="class-age">Ages 15 &amp; over</div></li>
    <li><svg width="12" height="10"><path d="M0 0 12 5 0 10 3 5Z" fill="#d10a0a"/></svg><div class="class-name">Wing Chun</div><div class="class-age">Ages 13 &amp; over</div></li>
  </ul>
  <div class="more">More</div>
</article>

<article class="abs card" style="left:384px">
  <h2 class="card-head" style="font-weight:400">How It Works</h2>
  <div class="video">
    <svg width="213" height="203" viewBox="0 0 213 203">
      <path d="M101 69 125 91 101 113Z" fill="#fff"/>
      <rect x="7" y="179" width="199" height="7" fill="#a7c400"/>
      <rect x="18" y="172" width="3" height="20" fill="#fff"/>
    </svg>
  </div>
  <p class="video-copy">Traditional Shaolin Kung Fu, Wing Chun Kung Fu, Tai Chi &amp; Qigong for all ages and physical capabilities.</p>
</article>

<article class="abs card" style="left:670px">
  <h2 class="card-head" style="font-weight:400">About Us</h2>
  <div class="about">
    <p><b>Kids Kung Fu</b> – ages 6 to 11. Practical, Responsible Instruction. Plus, we specialize in powerful character development skills in a positive environment. Kids learn self defence NOT fighting, anti bullying techniques.</p>
    <p><b>Youth Kung Fu</b> – ages 11 to 15. The ultimate way to Build Confidence, Self-Esteem, Self-Discipline, and Athletic Skills, while learning self defence in a tradition style Martial Arts.</p>
    <p><b>Adults Shaolin Kung Fu</b> - ages 15 &amp; over. Self defence utilizing great range of punches, kicks, joint-locking, throwing and grappling techniques.</p>
  </div>
  <div class="more">More</div>
</article>

<footer class="abs footer"></footer>
<h3 class="abs f-title" style="left:75px;top:950px;font-weight:400">Accreditation</h3>
<div class="abs badge" style="left:75px;width:52px;border-radius:50%;background:#c8a24a"></div>
<div class="abs badge" style="left:133px;top:997px;width:59px;height:40px;background:#eee"></div>
<div class="abs badge" style="left:199px;top:997px;width:51px;height:40px;background:#f3f3f3"></div>
<h3 class="abs f-title" style="left:75px;top:1060px;font-weight:400">Alliances</h3>
<div class="abs" style="left:75px;top:1091px;width:52px;height:60px;background:#8a7a5a"></div>

<div class="abs divider" style="left:290px"></div>
<h3 class="abs f-title" style="left:327px;top:950px;font-weight:400">Latest News &amp; Events</h3>
<ul class="abs news">
  <li><svg width="12" height="10"><path d="M0 0 12 5 0 10 3 5Z" fill="#d10a0a"/></svg>Kids Kung Fu Holiday Workshop 18thApril 2012 Kwoon Open Day 12th All welcome.</li>
  <li><svg width="12" height="10"><path d="M0 0 12 5 0 10 3 5Z" fill="#d10a0a"/></svg>Copper Heron Hosts: "A day with the masters". Grand Master Wei Lan to visit our Kwoon.</li>
  <li><svg width="12" height="10"><path d="M0 0 12 5 0 10 3 5Z" fill="#d10a0a"/></svg>See the "Timetable" page for new timetable and classes.</li>
</ul>
<div class="abs divider" style="left:651px"></div>

<h3 class="abs f-title" style="left:690px;top:950px;font-weight:400">Follow Us</h3>
<div class="abs follow">
  <div class="social-chip chip-blue">Fn</div>
  <div class="social-chip chip-red">Ct</div>
</div>
<div class="abs newsletter">Newsletter Download</div>

<div class="abs bottom">
  <span>Home &nbsp;| &nbsp;Programs &nbsp;| &nbsp;Timetable &nbsp;| &nbsp;Coaches &nbsp;| &nbsp;Member Zone &nbsp;| &nbsp;Contact Us</span>
  <span>© &nbsp;2012. All Rights Reserved. &nbsp; X48</span>
</div>

</div>
</body>
</html>
```